Corvane Photography Business Card Design

I need a business card designed for a photography business based in Perth, Western Australia called Corvane Photography.

We specialise in wedding, event photography and portrait photography.

The business card must borrow the style of the attached logo.

The hex codes for the colours in the logo are:
#ED1D85 - Pink
#89C23E - Green
#37282F - Black

The name on the card will be:
Name: Teodric
Phone: 0417360825
Website: www.corvanephotography-example.com.au
Facebook: corvanephotography

I am open and happy to accept creative concepts.

Industry/Entity Type

Business

```html
<!DOCTYPE html>
<html lang="en">
<head>
<meta charset="utf-8">
<title>Corvane Photography Business Card</title>
<link rel="stylesheet" href="https://fonts.googleapis.com/css2?family=Cinzel:wght@700&family=Questrial&display=swap">
<style>
  :root {
    --pink: #ED1D85;
    --green: #89C23E;
    --black: #37282F;
    --ink: #4a3a40;
    --title-ink: #5a4a50;
    --card: #ffffff;
    --backdrop: #d9d9d9;
  }
  * { box-sizing: border-box; margin: 0; padding: 0; }
  html, body {
    width: 1200px;
    height: 900px;
    overflow: hidden;
    background: var(--backdrop);
  }
  .canvas {
    position: relative;
    width: 1200px;
    height: 900px;
  }
  .card {
    position: absolute;
    top: 305px;
    width: 478px;
    height: 288px;
    background: var(--card);
    border-radius: 16px;
    overflow: hidden;
  }
  .card--front { left: 95px; }
  .card--back { left: 627px; }

  .brand-mark {
    position: absolute;
    left: 50%;
    border-radius: 50%;
    background: var(--pink);
    transform: translateX(-50%);
  }
  .card--front .brand-mark { top: 22px; width: 76px; height: 76px; }
  .card--back .brand-mark { top: 86px; width: 82px; height: 82px; }

  .brand-name {
    position: absolute;
    left: 0;
    right: 0;
    text-align: center;
    font-family: "Questrial", sans-serif;
    text-transform: uppercase;
    color: var(--title-ink);
    white-space: nowrap;
  }
  .card--front .brand-name {
    top: 117px;
    font-size: 12px;
    letter-spacing: 0.52em;
    padding-left: 0.52em;
  }
  .card--back .brand-name {
    top: 188px;
    font-size: 13px;
    letter-spacing: 0.55em;
    padding-left: 0.55em;
  }

  .person-name {
    position: absolute;
    top: 162px;
    left: 0;
    right: 0;
    text-align: center;
    font-family: "Cinzel", serif;
    font-weight: 700;
    font-size: 18px;
    letter-spacing: 0.04em;
    color: var(--ink);
  }

  .contact-list {
    position: absolute;
    top: 209px;
    left: 0;
    right: 0;
    list-style: none;
    text-align: center;
    font-family: "Questrial", sans-serif;
    color: var(--black);
  }
  .contact-item {
    display: flex;
    justify-content: center;
    align-items: center;
    gap: 5px;
    height: 18px;
    text-transform: uppercase;
    font-size: 11.5px;
    letter-spacing: 0.06em;
  }
  .contact-item--phone {
    font-size: 14px;
    letter-spacing: 0.04em;
    text-transform: none;
  }
  .contact-icon { width: 10px; height: 10px; flex: none; }
  .social-square {
    width: 9px;
    height: 9px;
    background: var(--green);
    border-radius: 1px;
    flex: none;
  }

  .colour-bands {
    position: absolute;
    left: 0;
    bottom: 0;
    width: 478px;
    height: 16px;
  }
</style>
</head>
<body>
<main class="canvas">

  <section class="card card--front" aria-label="Business card front">
    <span class="brand-mark" aria-hidden="true"></span>
    <p class="brand-name">Corvane Photography</p>
    <h1 class="person-name">Teodric</h1>
    <ul class="contact-list">
      <li class="contact-item contact-item--phone">
        <svg class="contact-icon" viewBox="0 0 10 10" aria-hidden="true">
          <rect width="10" height="10" rx="2" fill="var(--green)"/>
          <path d="M3 2.2c.4 0 .6.9.8 1.3.1.3-.5.6-.4.9.3.7.8 1.2 1.5 1.5.3.1.6-.5.9-.4.4.2 1.3.4 1.3.8 0 .6-.5 1.3-1.2 1.3C4 7.6 2.4 6 2.4 3.4c0-.7.1-1.2.6-1.2z" fill="#fff"/>
        </svg>
        <span>0417360825</span>
      </li>
      <li class="contact-item">
        <span class="social-square" aria-hidden="true"></span>
        <span>corvanephotography</span>
      </li>
      <li class="contact-item">
        <svg class="contact-icon" viewBox="0 0 10 10" aria-hidden="true">
          <circle cx="5" cy="5" r="4.5" fill="var(--green)"/>
          <g fill="none" stroke="#fff" stroke-width="0.7">
            <ellipse cx="5" cy="5" rx="2" ry="4.5"/>
            <line x1="0.5" y1="5" x2="9.5" y2="5"/>
            <line x1="5" y1="0.5" x2="5" y2="9.5"/>
          </g>
        </svg>
        <span>www.corvanephotography-example.com.au</span>
      </li>
    </ul>
    <svg class="colour-bands" viewBox="0 0 478 16" aria-hidden="true">
      <polygon points="0,0 158,0 153,16 0,16" fill="var(--pink)"/>
      <polygon points="160,0 322,0 317,16 155,16" fill="var(--green)"/>
      <polygon points="324,0 478,0 478,16 319,16" fill="var(--black)"/>
    </svg>
  </section>

  <section class="card card--back" aria-label="Business card back">
    <span class="brand-mark" aria-hidden="true"></span>
    <p class="brand-name">Corvane Photography</p>
  </section>

</main>
</body>
</html>
```